Divorce Lawyer Creative Business Card Design Project

Need a fresh look for our business cards that incorporates our current logo. We have three attorneys and six staff. Some will also use a Q/R Code (which is personal to the staff member) and that should be incorporated into the design so that we have a "with Q/R Code option" and a "without Q/R Code option"
While our business is serious and we want to be professional, we also welcome a bit of creativity and "fun." See http://cardowlet.example/creative-business-card-for-a-divorce-lawyer/ for a unique divorce lawyer business card. It is cool but the card itself is boring...
We add new people, change titles, some of our staff get married (and divorced) and have name changes and we need the ability to use a design template that you provide to make these changes ourselves. We usually print our cards at Plumo Press.
I have uploaded a file that contains a sample of our current front and back of the business card as well as a sample Q/R Contact code to be included on a card. Obviously, we like the design that we have which should give you a feel for us but we are ready for a fresh look.
If you can't provide a design that we can manipulate, we will need .eps, .pdf, and .jpg files for three attorneys and six staff.
Updates
- Layout for this card is really nice: http://blog.inkhollow.example/wp-content/uploads/2013/03/torva-business-card.jpg
- This is creative: http://pinboardly.example/pin/572810394628150443/ but I don't really like it.
- Plastic is kind of cool: http://pinboardly.example/pin/572810394628937216/
- DISLIKE: http://promoglobe.example/sites/default/files/styles/media/public/images/Lawyerbusinesscard.jpg?itok=ZrTmWe-k
- This is really cool but I fear the printing costs would be too high: http://pinboardly.example/pin/46192837504618352/
- I am not opposed to different but similar designs: See http://www.folioverse.example/gallery/ZEP-Business-Cards/8263045
Industry/Entity Type
Lawyer
Requirements
Must have
- Our Logo
Person's Full Name
Title
Phone #
Fax #
Email
Web Address

```html
<!DOCTYPE html>
<html lang="en">
<head>
<meta charset="utf-8">
<title>Birchway Family Law – Stationery</title>
<link rel="stylesheet" href="https://fonts.googleapis.com/css2?family=Open+Sans:wght@300;400&display=swap">
<style>
  :root {
    --backdrop: #3a3a3c;
    --charcoal: #2a2a2a;
    --orange: #f39020;
    --paper: #ffffff;
    --rule: #7a7a7a;
    --ink: #111111;
    --muted: #9a9a9a;
  }
  * { box-sizing: border-box; margin: 0; padding: 0; }
  html, body { width: 1200px; height: 900px; overflow: hidden; }
  body {
    background: var(--backdrop);
    font-family: "Open Sans", sans-serif;
    position: relative;
  }
  .piece { position: absolute; box-shadow: 0 3px 10px rgba(0,0,0,.35); overflow: hidden; }

  /* Firm wordmark (single colour, single weight) */
  .wordmark {
    position: absolute; display: flex; align-items: center; gap: 7px;
    font-size: 12px; font-weight: 400; white-space: nowrap;
  }
  .wordmark__square { width: 9px; height: 9px; background: currentColor; }

  /* Letterhead */
  .letterhead { left: 40px; top: 60px; width: 400px; height: 518px; background: var(--paper); }
  .letterhead .wordmark { left: 34px; top: 38px; color: var(--orange); }
  .letterhead__band {
    position: absolute; left: 0; right: 0; top: 92px; height: 46px;
    background: var(--orange); color: var(--paper);
    font-weight: 300; font-size: 17px; line-height: 46px; padding-left: 34px;
  }
  .letterhead__footer {
    position: absolute; left: 0; right: 0; bottom: 26px;
    text-align: center; font-size: 9px; color: var(--muted); font-weight: 300;
    white-space: nowrap;
  }
  .letterhead__footer .sep { margin: 0 8px; }
  .letterhead__footer .web { color: var(--ink); }
  .letterhead__footer .web em { font-style: normal; color: var(--orange); }

  /* Orange card */
  .card-orange { left: 40px; top: 620px; width: 350px; height: 200px; background: var(--orange); }
  .card-orange svg { position: absolute; left: 0; top: 0; }
  .card-orange .wordmark { left: 28px; bottom: 26px; color: var(--paper); }

  /* Vertical cards */
  .card { top: 130px; width: 210px; height: 368px; }
  .card--dark { left: 480px; background: var(--charcoal); color: var(--paper); }
  .card--light { left: 710px; background: var(--paper); color: var(--ink); }
  .card--back { left: 940px; background: var(--charcoal); }
  .card__rule { position: absolute; left: 62px; top: 0; width: 1.5px; height: 215px; background: var(--rule); }
  .card__tab { position: absolute; left: 0; bottom: 18px; width: 5px; height: 34px; background: var(--orange); }
  .card__name {
    position: absolute; right: 18px; bottom: 92px; text-align: right;
    font-size: 14px; font-weight: 400; line-height: 1.3; white-space: nowrap;
  }
  .card__title { display: block; font-size: 10px; font-weight: 300; }
  .card .wordmark { left: 18px; bottom: 22px; font-size: 10px; gap: 6px; }
  .card--dark .wordmark { color: var(--paper); }
  .card--light .wordmark { color: var(--orange); }
  .card .wordmark__square { width: 7px; height: 7px; }

  /* QR-code option: plain placeholder square */
  .card__qr {
    position: absolute; right: 18px; top: 168px; width: 56px; height: 56px;
    background: var(--paper);
  }

  .card__contact {
    position: absolute; left: 0; right: 0; bottom: 0; height: 128px;
    background: var(--orange); color: var(--paper);
    font-size: 8.5px; font-weight: 300; text-align: center; line-height: 1.55;
    padding-top: 26px; white-space: nowrap;
  }
  .card__contact p + p { margin-top: 6px; }
</style>
</head>
<body>

  <section class="piece letterhead" aria-label="Letterhead">
    <p class="wordmark"><span class="wordmark__square"></span>Birchway Family Law</p>
    <div class="letterhead__band">Managing Attorney</div>
    <p class="letterhead__footer">
      Suite G, 218 alder street, Ashford NC 28550<span class="sep">|</span><span class="web">www.<em>Birchwayfamilylaw</em>.example</span>
    </p>
  </section>

  <section class="piece card-orange" aria-label="Card back, orange">
    <svg width="350" height="200" viewBox="0 0 350 200" aria-hidden="true">
      <line x1="0" y1="58" x2="300" y2="58" stroke="#6e6e6e" stroke-width="1.5"/>
    </svg>
    <p class="wordmark"><span class="wordmark__square"></span>Birchway Family Law</p>
  </section>

  <section class="piece card card--dark" aria-label="Card front, dark">
    <span class="card__rule"></span>
    <p class="card__name">Daniel Reed Hollis<span class="card__title">Managing Attorney</span></p>
    <p class="wordmark"><span class="wordmark__square"></span>Birchway Family Law</p>
    <span class="card__tab"></span>
  </section>

  <section class="piece card card--light" aria-label="Card front, light">
    <span class="card__rule"></span>
    <p class="card__name">Daniel Reed Hollis<span class="card__title">Managing Attorney</span></p>
    <p class="wordmark"><span class="wordmark__square"></span>Birchway Family Law</p>
    <span class="card__tab"></span>
  </section>

  <section class="piece card card--back" aria-label="Card back with contact details and QR-code option">
    <span class="card__rule"></span>
    <span class="card__qr" role="img" aria-label="Personal QR contact code area"></span>
    <div class="card__contact">
      <p>Counsel Court-Suite G 218 Alder street<br>Ashford, NC 28550</p>
      <p>Phone - 910 555 0148 | Fax - 910 555 0149<br>Email - dhollis@birchwayfamilylaw.example<br>www.Birchwayfamilylaw.example</p>
    </div>
  </section>

</body>
</html>
```